Blister Packaging Design for a Mouthguard

I need a clean and professional design for a mouthguard packaging.
the design should be clean, mostly black, white and grey. it should show our logo "VORTANEL". The Frontside schould show the German word "MUNDSCHUTZ" and smaller the Term "Mouthguard". the pfont should also show some parts in german flag colors to show we are a german company. at some place there has to be a place where the different style can be inserted. 4 main styles will be: "STRGL", "SPINDLE", "GLIMMER", "NEBEL TOR"
on the backside there need to be a place for the barcode and our company adress, detailes product description an maybe a picture of a drawed mouthguard.
Attached as well a finished design from some other company, just to show where the mouthguard will be placed in the packaging.
Target Market(s)
Boxing and Fighting sports in general
Industry/Entity Type
sport, fighting sports
Colors
Designer to choose only greyscale colors for use in the design.
Requirements
Must have
- clean and professional design
Nice to have
- German flag/Colors somewhere embedded on the front of the packaging
Should not have
- not too colorful

```html
<!DOCTYPE html>
<html lang="de">
<head>
<meta charset="utf-8">
<title>VORTANEL Mundschutz – Blisterkarte</title>
<link rel="stylesheet" href="https://fonts.googleapis.com/css2?family=Alfa+Slab+One&family=Montserrat:wght@600;700;800&family=Roboto+Condensed:wght@400;700&display=swap">
<style>
  :root{
    --paper:#ffffff;
    --back-top:#7b7b7b;
    --back-body:#e3e3e3;
    --front-top:#5c5c5c;
    --front-body:#262626;
    --ink:#1e1e1e;
    --logo-light:#d9d9d9;
    --hole:#ffffff;
    --keyline:#29a8e0;
    --guide:#8a8a8a;
    --de-black:#1a1a1a;
    --de-red:#dd3b26;
    --de-gold:#f5b13d;
    --us-blue:#3c4f9a;
    --us-red:#d9473f;
  }
  *{margin:0;padding:0;box-sizing:border-box}
  html,body{width:1200px;height:885px;overflow:hidden;background:var(--paper)}
  .canvas{position:relative;width:1200px;height:885px}
  .card{position:absolute;top:46px;width:542px;height:776px;box-shadow:5px 5px 7px rgba(0,0,0,.35);overflow:hidden}
  .card--back{left:43px;background:var(--back-body)}
  .card--front{left:614px;background:var(--front-body)}
  .card svg.bg{position:absolute;inset:0}
  .abs{position:absolute}
  .brand{font-family:"Montserrat",sans-serif;font-weight:800;font-size:15px;letter-spacing:1px;color:var(--logo-light);display:flex;align-items:center;gap:6px;white-space:nowrap}
  .brand__dot{width:9px;height:9px;background:var(--logo-light)}
  .lang{font-family:"Roboto Condensed",sans-serif;font-size:13px;color:var(--ink);display:flex;align-items:center;gap:6px}
  .flag{display:inline-block;width:35px;height:21px}
  .flag--de{background:linear-gradient(var(--de-black) 0 33.3%,var(--de-red) 33.3% 66.6%,var(--de-gold) 66.6%)}
  .flag--us{width:31px;background:linear-gradient(to right,var(--us-blue) 0 45%,transparent 45%),repeating-linear-gradient(var(--us-red) 0 3px,#fff 3px 6px)}
  .copy{font-family:"Roboto Condensed",sans-serif;font-size:7.6px;line-height:11.2px;color:var(--ink);letter-spacing:-.1px}
  .copy ul{list-style:none}
  .copy li{padding-left:15px;position:relative}
  .copy li::before{content:"";position:absolute;left:1px;top:3.5px;width:4px;height:4px;background:#555}
  .copy h4{font-weight:700;font-size:7.6px}
  .copy ol{list-style:none}
  .copy ol li{padding-left:10px}
  .copy ol li::before{display:none}
  .copy ol li span{position:absolute;left:0}
  .part-label{font-family:"Roboto Condensed",sans-serif;font-size:10.5px;line-height:13px;color:var(--ink)}
  .maker{font-family:"Roboto Condensed",sans-serif;font-size:7.4px;line-height:12px;color:var(--ink)}
  .maker strong{font-family:"Montserrat",sans-serif;font-weight:700;font-size:9px;display:block}
  .illustration{background:linear-gradient(135deg,#f2f2f2,#cfcfcf);border-radius:30px 8px 40px 10px}
  .barcode-field{background:#fff;border:1px solid #bdbdbd}
  .style-label{font-family:"Montserrat",sans-serif;font-weight:700;color:#fff;white-space:nowrap}
  .map-fill{background:linear-gradient(var(--de-black) 0 40%,var(--de-red) 40% 70%,var(--de-gold) 70%);border-radius:40% 30% 25% 35%}
</style>
</head>
<body>
<div class="canvas">

  <!-- Back side -->
  <section class="card card--back">
    <svg class="bg" width="542" height="776" viewBox="0 0 542 776">
      <path d="M0 0H542V201Q271 135 0 201Z" fill="var(--back-top)"/>
      <rect x="43" y="38" width="455" height="692" rx="14" fill="none" stroke="var(--keyline)" stroke-width="1.2" stroke-dasharray="5 3"/>
      <circle cx="272" cy="77" r="19" fill="var(--hole)"/>
      <rect x="200" y="72" width="146" height="29" rx="14.5" fill="var(--hole)"/>
      <circle cx="421" cy="115" r="41" fill="#e4e4e4" stroke="#bdbdbd" stroke-width="2"/>
      <circle cx="421" cy="115" r="30" fill="none" stroke="#b0b0b0" stroke-width="1"/>
    </svg>

    <div class="abs brand" style="left:68px;top:98px"><span class="brand__dot"></span>VORTANEL</div>

    <div class="abs lang" style="left:59px;top:209px">Deutsch <span class="flag flag--de"></span></div>
    <div class="abs lang" style="left:286px;top:209px">English <span class="flag flag--us" role="img" aria-label="Flagge der USA"></span></div>

    <div class="abs copy" style="left:59px;top:240px;width:210px">
      <ul>
        <li>FLEX Core Mundschutz.</li>
        <li>Material: EVA-Material.</li>
        <li>Schutzhülle enthalten.</li>
        <li>Schützt vor Stößen.</li>
        <li>Alle Arten von Kontaktsportarten.</li>
        <li>Nicht mit Zahnspangen verwenden.</li>
      </ul>
      <h4 style="margin-top:11px">Formschritte :</h4>
      <ol>
        <li><span>1 -</span>Beginnen Sie mit kochendem Wasser.</li>
        <li><span>2 -</span>Gießen Sie 200 ml in eine Schüssel und lassen Sie es 30 Sekunden lang stehen.</li>
        <li><span>3 -</span>Legen Sie den Mundschutz für 90 bis 120 Sekunden in das Wasser.</li>
        <li><span>4 -</span>Richten Sie den Mundschutz auf die Mitte Ihres Mundes aus und drücken Sie ihn fest nach oben. Beißen Sie dann sanft zu, während Sie aspirieren.</li>
        <li><span>5 -</span>Drücken Sie mit Ihren Fingern den Rand des Mundschutzes in Richtung des Zahnfleischrands.</li>
        <li><span>6 -</span>Legen Sie den Mundschutz für 30 Sekunden in eine Schüssel mit kaltem Wasser.</li>
      </ol>
      <h4 style="margin-top:11px">WARNHINWEISE:</h4>
      <p>Sportliches Training kann zu Verletzungen führen. Schutzausrüstung kann nicht alle Verletzungen verhindern, kann aber in manchen Fällen den Schaden verringern. Trainieren Sie niemals ohne Rücksprache mit Ihrem Arzt. Überprüfen Sie Ihre Ausrüstung immer vor dem Gebrauch. Wenn Sie Mängel feststellen, verwenden Sie das Produkt nicht.</p>
    </div>

    <div class="abs copy" style="left:286px;top:240px;width:200px">
      <ul>
        <li>FLEX Core Mouth Guard.</li>
        <li>Material : EVA Material.</li>
        <li>Protective case included.</li>
        <li>Protects against impact.</li>
        <li>All types of contact sports.</li>
        <li>Do not use with braces.</li>
      </ul>
      <h4 style="margin-top:11px">Molding Steps :</h4>
      <ol>
        <li><span>1 -</span>Start by boiling water.</li>
        <li><span>2 -</span>Pour 200ml into bowl and leave for 30 seconds.</li>
        <li><span>3 -</span>Place the mouth guard in the water for 90 to 120 seconds.</li>
        <li><span>4 -</span>Align the mouth guard with the centre of your mouth and press it upwards firmly, then bite down gently while aspiring.</li>
        <li><span>5 -</span>Use your fingers to push the edge of the mouth guard towards the gum line.</li>
        <li><span>6 -</span>Place the mouth guard in a bowl of cold water for 30 seconds.</li>
      </ol>
      <h4 style="margin-top:44px">WARNINGS:</h4>
      <p>Sports training can lead to injuries. Protective equipment will not eliminate all injuries, but may reduce the damage in some cases. Never practice without consulting your doctor. Always check your equipment before use. If you notice any defects, do not use the product.</p>
    </div>

    <div class="abs illustration" style="left:64px;top:556px;width:130px;height:160px" role="img" aria-label="Linienzeichnung des Mundschutzes mit Gelkern und Anti-Schock-Körper"></div>
    <div class="abs part-label" style="left:152px;top:557px">Stoßdämpfendes Gel<br>Shock Absorbing Gel</div>
    <div class="abs part-label" style="left:154px;top:689px">Anti-Schock-Körper<br>Anti-Shock Body</div>

    <div class="abs maker" style="left:284px;top:584px">
      Manufactured By :
      <strong>VORTANEL</strong>
      Lorem IpsumLorem IpsumLorem<br>
      info@vortanel.de | www.vortanel.de
    </div>
    <svg class="abs" style="left:287px;top:651px" width="14" height="14" viewBox="0 0 14 14"><circle cx="7" cy="7" r="5.5" fill="none" stroke="#333" stroke-width="1.2"/></svg>
    <div class="abs barcode-field" style="left:287px;top:671px;width:176px;height:40px" role="img" aria-label="Feld für Barcode"></div>
  </section>

  <!-- Front side -->
  <section class="card card--front">
    <svg class="bg" width="542" height="776" viewBox="0 0 542 776">
      <path d="M0 0H542V201Q271 150 0 201Z" fill="var(--front-top)"/>
      <rect x="43" y="38" width="455" height="692" rx="14" fill="none" stroke="var(--keyline)" stroke-width="1.2" stroke-dasharray="5 3"/>
      <circle cx="272" cy="77" r="19" fill="var(--hole)"/>
      <rect x="200" y="72" width="146" height="29" rx="14.5" fill="var(--hole)"/>
      <path d="M84 273Q272 240 459 273V520Q420 600 272 688Q124 600 84 520Z" fill="none" stroke="var(--guide)" stroke-width="1.1" stroke-dasharray="5 4"/>
      <g transform="translate(84 243) rotate(-9) scale(1 1.55)" font-family="'Alfa Slab One',serif">
        <text x="0" y="0" font-size="52" textLength="372" lengthAdjust="spacingAndGlyphs" fill="#fff" stroke="#000" stroke-width="3" paint-order="stroke">MUNDSCHUTZ</text>
      </g>
      <g transform="translate(300 236) rotate(-9)" font-family="'Montserrat',sans-serif" font-weight="800">
        <text x="0" y="0" font-size="20" textLength="154" lengthAdjust="spacingAndGlyphs" fill="#fff">MOUTHGUARD</text>
      </g>
    </svg>

    <div class="abs brand" style="left:62px;top:98px"><span class="brand__dot"></span>VORTANEL</div>

    <div class="abs style-label" style="left:72px;top:656px;font-size:14px">Style</div>
    <div class="abs style-label" style="left:72px;top:672px;font-size:28px;font-weight:600;letter-spacing:1px">NEBEL TOR</div>

    <div class="abs style-label" style="left:346px;top:666px;font-size:14px;line-height:17px">German<br>Made</div>
    <div class="abs map-fill" style="left:405px;top:615px;width:68px;height:86px" role="img" aria-label="Umriss von Deutschland in den Farben Schwarz, Rot und Gold"></div>
  </section>

</div>
</body>
</html>
```